Business Card Stationary and shirt design for Electrical Company
Corbishaw Electric LLC
Business Card Stationary and shirt design for Electrical Company - Construction
Creative Brief
Bright & Fun-filled
Owner
614 Linwood Avenue Jersey City, NJ 07305
1-855-48AMPRO
corbishawelectricllc@brivanmail.com
www.corbishawelectric-example.com
Highly rated : TradeRankr, Zorvik, NestGauge residential, commercial, industrial
Name of Business Logo web adress simple yet eye catching back (ill leave it up to the designer)

```html
<!DOCTYPE html>
<html lang="en">
<head>
<meta charset="utf-8">
<title>Corbishaw Electric LLC — Stationery Set</title>
<link href="https://fonts.googleapis.com/css2?family=Poppins:wght@400;600;700&display=swap" rel="stylesheet">
<style>
  :root{
    --navy:#1e2843;
    --green:#7cc142;
    --paper:#ffffff;
    --ink:#3a3f4a;
    --muted:#8a8f98;
    --rule:#d9dce1;
    --stage:#ececec;
  }
  *{box-sizing:border-box;margin:0;padding:0}
  html,body{width:1200px;height:578px;overflow:hidden}
  body{background:var(--stage);font-family:"Poppins",sans-serif;color:var(--ink);position:relative}
  .piece{position:absolute;background:var(--paper);box-shadow:0 2px 6px rgba(0,0,0,.18);overflow:hidden}

  .brand{display:flex;align-items:center;gap:6px;font-weight:700;color:var(--navy);line-height:1;white-space:nowrap}
  .brand .mark{background:var(--green);flex:none}
  .brand.on-dark{color:#fff}
  .brand.stacked{line-height:1.05}

  .band{position:absolute;left:0;right:0;bottom:0;background:var(--navy);color:#fff;font-size:8px;display:flex;align-items:center;justify-content:flex-end;padding-right:10px;white-space:nowrap}
  .band::before{content:"";position:absolute;left:0;right:0;top:-4px;height:4px;background:var(--green)}

  /* business cards */
  .card{width:187px;height:92px}
  .card-front{left:53px;top:120px}
  .card-front .brand{position:absolute;left:10px;top:12px;font-size:11px}
  .card-front .brand .mark{width:14px;height:14px}
  .card-front .contact{position:absolute;left:10px;top:38px;font-size:5px;line-height:1.5;color:var(--muted)}
  .card-front .band{height:20px;font-size:6px;gap:4px}
  .card-front .band b{font-weight:600}
  .card-back{background:var(--navy)}
  .card-back.one{left:53px;top:228px}
  .card-back.two{left:53px;top:348px;height:103px}
  .card-back .brand{position:absolute;left:14px;top:22px;font-size:11px}
  .card-back .brand .mark{width:15px;height:15px}
  .card-back .tag{position:absolute;left:14px;bottom:14px;font-size:5.5px;color:var(--green);letter-spacing:.3px}
  .card-back .rated{position:absolute;left:14px;bottom:24px;font-size:5px;color:#c7ccd6}
  .card-back .stripe{position:absolute;right:0;top:0;bottom:0;width:6px;background:var(--green)}

  /* letter sheets */
  .sheet{top:38px;width:264px;height:495px}
  .fax{left:269px}
  .letter{left:547px}
  .sheet .brand{position:absolute;left:18px;top:20px;font-size:13px}
  .sheet .brand .mark{width:22px;height:22px}
  .sheet .band{height:24px;font-size:7px}
  .fax-fields{position:absolute;left:18px;right:18px;top:80px;display:grid;grid-template-columns:1fr 1fr;column-gap:14px;row-gap:8px;font-size:7px;color:var(--navy)}
  .fax-fields span{border-bottom:1px solid var(--rule);padding-bottom:5px}
  .fax .comments{position:absolute;left:18px;top:188px;font-size:7px;color:var(--navy)}
  .letter .contact{position:absolute;right:16px;top:20px;font-size:5px;line-height:1.6;color:var(--muted);width:92px}

  /* envelopes & slip */
  .env-back{left:823px;top:120px;width:214px;height:118px}
  .env-back .flap{position:absolute;inset:0}
  .env-back .brand{position:absolute;left:50%;top:64px;transform:translateX(-50%);font-size:8px}
  .env-back .brand .mark{width:10px;height:10px}
  .env-front{left:830px;top:247px;width:207px;height:113px}
  .env-front .brand{position:absolute;left:10px;top:10px;font-size:9px}
  .env-front .brand .mark{width:11px;height:11px}
  .env-front .addr{position:absolute;left:10px;top:28px;font-size:4.5px;color:var(--muted)}
  .env-front .web{position:absolute;right:12px;bottom:26px;font-size:6px;color:var(--navy)}
  .env-front .band{height:14px}
  .slip{left:871px;top:372px;width:238px;height:108px}
  .slip .brand{position:absolute;left:12px;top:14px;font-size:9px}
  .slip .brand .mark{width:12px;height:12px}
  .slip .band{top:12px;bottom:auto;left:150px;height:16px;font-size:5px;padding-right:8px}
  .slip .band::before{display:none}
  .slip .contact{position:absolute;left:12px;top:36px;font-size:4.5px;line-height:1.6;color:var(--muted)}
  .slip .foot{position:absolute;left:0;right:0;bottom:0;height:10px;background:var(--navy)}
  .slip .foot::before{content:"";position:absolute;left:0;right:0;top:-3px;height:3px;background:var(--green)}
</style>
</head>
<body>

  <!-- business card front -->
  <div class="piece card card-front">
    <div class="brand"><span class="mark"></span>Corbishaw Electric LLC</div>
    <div class="contact">
      614 Linwood Avenue Jersey City, NJ 07305<br>
      1-855-48AMPRO<br>
      corbishawelectricllc@brivanmail.com<br>
      www.corbishawelectric-example.com
    </div>
    <div class="band"><b>Jordan Pell</b> Owner</div>
  </div>

  <!-- business card backs -->
  <div class="piece card card-back one">
    <div class="brand on-dark"><span class="mark"></span>Corbishaw Electric LLC</div>
    <div class="rated">Highly rated: TradeRankr · Zorvik · NestGauge</div>
    <div class="tag">Residential · Commercial · Industrial</div>
    <div class="stripe"></div>
  </div>
  <div class="piece card card-back two">
    <div class="brand on-dark"><span class="mark"></span>Corbishaw Electric LLC</div>
    <div class="rated">Highly rated: TradeRankr · Zorvik · NestGauge</div>
    <div class="tag">Residential · Commercial · Industrial</div>
    <div class="stripe"></div>
  </div>

  <!-- fax cover sheet -->
  <div class="piece sheet fax">
    <div class="brand stacked"><span class="mark"></span><span>Corbishaw<br>Electric LLC</span></div>
    <div class="fax-fields">
      <span>TO:</span><span>FROM:</span>
      <span>FAX:</span><span>PAGES:</span>
      <span>PHONE:</span><span>DATE:</span>
      <span>RE:</span><span>CC:</span>
    </div>
    <div class="comments">COMMENTS:</div>
    <div class="band"></div>
  </div>

  <!-- letterhead -->
  <div class="piece sheet letter">
    <div class="brand stacked"><span class="mark"></span><span>Corbishaw<br>Electric LLC</span></div>
    <div class="contact">
      614 Linwood Avenue<br>Jersey City, NJ 07305<br>
      1-855-48AMPRO<br>
      corbishawelectricllc@brivanmail.com
    </div>
    <div class="band">www.corbishawelectric-example.com</div>
  </div>

  <!-- envelope back -->
  <div class="piece env-back">
    <svg class="flap" viewBox="0 0 214 118" preserveAspectRatio="none" aria-hidden="true">
      <polygon points="0,0 214,0 107,52" fill="#1e2843"/>
      <polyline points="0,0 107,52 214,0" fill="none" stroke="#7cc142" stroke-width="2"/>
    </svg>
    <div class="brand"><span class="mark"></span>Corbishaw Electric LLC</div>
  </div>

  <!-- envelope front -->
  <div class="piece env-front">
    <div class="brand"><span class="mark"></span>Corbishaw Electric LLC</div>
    <div class="addr">614 Linwood Avenue Jersey City, NJ 07305</div>
    <div class="web">www.corbishawelectric-example.com</div>
    <div class="band"></div>
  </div>

  <!-- compliment slip -->
  <div class="piece slip">
    <div class="brand"><span class="mark"></span>Corbishaw Electric LLC</div>
    <div class="band">Corbishaw Electric LLC</div>
    <div class="contact">
      614 Linwood Avenue Jersey City, NJ 07305<br>
      1-855-48AMPRO<br>
      corbishawelectricllc@brivanmail.com
    </div>
    <div class="foot"></div>
  </div>

</body>
</html>
```